New Packaging Design Project for Matcha Green Tea

**I've added an image called 'Sizing example', this is to show you the size of the label compared to the pack. Currently we are using full size labels for the pack and they are too difficult to apply.
Hi. I need a new label creating for a 100g pack of stunning organic premium grade Matcha tea.
The label needs to be 69mm by 88.9mm on the finished product and will be placed on a foil pack which is somewhat larger than the label.
Needs to include the text:
"Matcha Green Tea"
"Organic Japanese Premium Grade"
"Perfect for drinking, blending and baking"
"100g"
Attaching our logo and the KPV certification which both need to be on the label.
You can see our other products at www.leafhollowco.co.uk
You key with this product is that we need it to stand out on Bazolia. There are many, many other Matcha products in foil packs, so this needs to be a bold and fresh design. My suggestion is to test the design by editing it into a screenshot of the Bazolia search page for matcha tea to see if it stands out.
Target Market(s)
Affluent health conscious individuals. Those with busy life, such as executives or parents,. Those with an active life, such as triathletes, yoga, cyclists. Those with a aspirational life, i.e. they want to have quality in their life and they aspire to have the latest trends.
Requirements
Must have
- Stand out design. Clear, clean, crisp.
- Our green colour is #63A802 / 99 / 168 / 2. C41, M0, Y99, K34
- We also sometimes use #144400- R: 20 G: 68 B: 0
Nice to have
- Could either show how the product is used - i.e. lifestyle or just show the quality of the product.
- Could show the product in a ceremonial style bowl, a matcha latte or being blended or used for baking. Could even show all of these, so long as it doesn't look 'busy'.
Should not have
- Clutter, too many things going on.

```html
<!DOCTYPE html>
<html lang="en">
<head>
<meta charset="utf-8">
<title>Leafhollow Matcha Green Tea Label</title>
<link href="https://fonts.googleapis.com/css2?family=Cinzel:wght@700;900&family=Questrial&display=swap" rel="stylesheet">
<style>
  :root {
    --canvas-bg: #e9e9e9;
    --label-white: #ffffff;
    --label-silver: #dcdcdc;
    --brand-green: #63a802;
    --tea-green: #1f8a2c;
    --deep-green: #144400;
    --ink: #111111;
    --text-dark: #222222;
    --photo-sky: #dfe6e4;
    --photo-hills: #7fa85a;
    --photo-field: #9cc24a;
    --photo-mat: #b9ae86;
    --badge-green: #1f7a2c;
  }
  * { margin: 0; padding: 0; box-sizing: border-box; }
  html, body {
    width: 1200px;
    height: 1200px;
    overflow: hidden;
    background: var(--canvas-bg);
  }
  .canvas {
    position: relative;
    width: 1200px;
    height: 1200px;
  }
  .label {
    position: absolute;
    left: 270px;
    top: 58px;
    width: 660px;
    height: 1084px;
    background: linear-gradient(100deg, var(--label-silver) 0%, var(--label-white) 22%, var(--label-white) 80%, #f0f0f0 100%);
    overflow: hidden;
    box-shadow: 0 2px 10px rgba(0,0,0,0.12);
  }
  .brand-name {
    position: absolute;
    top: 78px;
    left: 0;
    width: 100%;
    text-align: center;
    font-family: "Questrial", sans-serif;
    font-size: 82px;
    color: var(--brand-green);
    letter-spacing: 1px;
  }
  .grade {
    position: absolute;
    top: 198px;
    width: 100%;
    text-align: center;
    font-family: "Questrial", sans-serif;
    font-size: 30px;
    color: var(--text-dark);
  }
  .product-title {
    position: absolute;
    top: 300px;
    width: 100%;
    text-align: center;
    font-family: "Cinzel", serif;
    font-weight: 900;
    font-size: 78px;
    color: var(--ink);
    letter-spacing: 1px;
  }
  .product-subtitle {
    position: absolute;
    top: 404px;
    width: 100%;
    text-align: center;
    font-family: "Cinzel", serif;
    font-weight: 700;
    font-size: 44px;
    color: var(--tea-green);
    letter-spacing: 2px;
  }
  .uses {
    position: absolute;
    top: 508px;
    width: 100%;
    text-align: center;
    font-family: "Questrial", sans-serif;
    font-size: 23px;
    color: var(--text-dark);
  }
  .hero-photo {
    position: absolute;
    left: 0;
    top: 563px;
    width: 100%;
    height: 521px;
    background: linear-gradient(180deg,
      var(--photo-sky) 0%,
      var(--photo-hills) 16%,
      var(--photo-field) 38%,
      #6f8f3a 62%,
      var(--photo-mat) 78%,
      #a39a74 100%);
  }
  .net-weight {
    position: absolute;
    right: 28px;
    top: 888px;
    font-family: "Questrial", sans-serif;
    font-size: 42px;
    color: var(--label-white);
  }
  .cert-badge {
    position: absolute;
    left: 30px;
    top: 1000px;
  }
</style>
</head>
<body>
<main class="canvas">
  <section class="label">
    <div class="brand-name">Leafhollow</div>
    <p class="grade">Organic Japanese Premium Grade</p>
    <h1 class="product-title">MATCHA</h1>
    <h2 class="product-subtitle">GREEN TEA</h2>
    <p class="uses">Perfect for drinking, blending and baking</p>
    <div class="hero-photo" role="img" aria-label="Photo of a pyramid of matcha powder in a black dish beside a glass cup of matcha on a bamboo mat, with green tea fields and hills behind"></div>
    <div class="net-weight">100g</div>
    <svg class="cert-badge" width="84" height="84" viewBox="0 0 84 84" role="img" aria-label="KPV organic certification badge">
      <circle cx="42" cy="42" r="38" fill="none" stroke="var(--badge-green)" stroke-width="6"/>
    </svg>
  </section>
</main>
</body>
</html>
```